Real Estate Company Looking for Business Card Designs for 3 Executives

Hello!
Thanks so much for considering our project! We are a real estate investment company located in Edmonton, Alberta called Marlbeck Group of Companies. We invest/develop both commercial and residential real estate and are looking to create 3 DOUBLE-SIDED business cards for 3 top executives in the company! (for some reason it won't let us select the double-sided option, but yes, the cards are double sided and would be happy to tip extra)

We have certain guidelines that we want our business cards to for sure follow - the back of the Business card has to be the Black Background Version of the Logo which has already been designed and linked as a file (first file). We want the entire back of the card to simply just be the black background logo. In terms of the front of the card, would like to see a smaller version of the white background logo (linked as the second file) in the top left hand corner - of course, feel free to get creative and we can make revisions together along the way! and Then after that, just text. We want the card to be sharp, clean, easy on the eyes and highly professional looking. We would like the card to include the Full name of the Company (Marlbeck Group of Companies), Name of the Person, Title, Phone, Email. If possible please provide the front part of the card for 3 people:

1) Marlbeck Group of Companies, Lena Okafor, Chief Financial Officer, 780-555-0162, lenaokafor@marlbeckgroup.example

2) Marlbeck Group of Companies, Tobias Okafor, Chief Executive Officer, 780-555-0148, tobiasokafor@marlbeckgroup.example

3) Marlbeck Group of Companies, Rui Dalton, Chief Operations Officer, 587-555-0193, ruidalton@marlbeckgroup.example

Thank you so much for considering our project & we look forward to seeing your designs!

```html
<!DOCTYPE html>
<html lang="en">
<head>
<meta charset="utf-8">
<title>Marlbeck Business Card</title>
<link href="https://fonts.googleapis.com/css2?family=Jost:wght@500&family=Karla:wght@400;600&display=swap" rel="stylesheet">
<style>
  :root {
    --bg: #e4e4e4;
    --paper: #ffffff;
    --ink: #111111;
    --grey: #6b6b6b;
    --night: #1f2022;
    --night-deep: #151617;
    --snow: #ffffff;
  }
  * { margin: 0; padding: 0; box-sizing: border-box; }
  html, body { width: 1200px; height: 1200px; overflow: hidden; }
  body { background: var(--bg); position: relative; font-family: "Karla", sans-serif; }

  .card { position: absolute; left: 150px; width: 900px; height: 513px; }
  .card-front { top: 57px; background: var(--paper); }
  .card-back { top: 630px; background: linear-gradient(180deg, var(--night), var(--night-deep)); }

  /* front */
  .front-brand {
    position: absolute; left: 91px; top: 183px; width: 250px; height: 150px;
    display: flex; flex-direction: column; align-items: center; justify-content: center;
  }
  .brand-mark { width: 34px; height: 34px; background: var(--ink); }
  .brand-name {
    font-family: "Jost", sans-serif; font-weight: 500; color: var(--ink);
    font-size: 30px; letter-spacing: 6px; padding-left: 6px; line-height: 1;
  }
  .front-brand .brand-name { margin-top: 18px; }
  .company-name {
    margin-top: 10px; font-size: 12.5px; letter-spacing: 1.6px; color: var(--grey);
    text-transform: uppercase; white-space: nowrap;
  }
  .divider { position: absolute; left: 383px; top: 183px; width: 1.5px; height: 150px; background: var(--ink); }
  .details { position: absolute; left: 420px; top: 180px; }
  .person-name { font-weight: 600; font-size: 32px; letter-spacing: 1px; color: var(--ink); line-height: 1.1; }
  .person-title { font-size: 19px; color: var(--grey); letter-spacing: 0.6px; margin-top: 4px; }
  .contact { list-style: none; margin-top: 17px; }
  .contact li { display: flex; align-items: center; gap: 9px; font-size: 19px; color: #444; letter-spacing: 0.4px; line-height: 25px; }
  .contact svg { width: 14px; height: 14px; fill: var(--ink); flex: none; }

  /* back */
  .back-brand {
    position: absolute; left: 0; right: 0; top: 140px;
    display: flex; flex-direction: column; align-items: center; gap: 28px;
  }
  .back-brand .brand-mark { width: 60px; height: 60px; background: var(--snow); }
  .back-brand .brand-name { color: var(--snow); font-size: 54px; letter-spacing: 12px; padding-left: 12px; }
  .back-web {
    position: absolute; left: 0; right: 0; top: 440px; text-align: center;
    color: var(--snow); font-size: 19px; letter-spacing: 3.5px; font-weight: 400;
  }
</style>
</head>
<body>
  <section class="card card-front">
    <div class="front-brand">
      <div class="brand-mark"></div>
      <div class="brand-name">MARLBECK</div>
      <div class="company-name">Marlbeck Group of Companies</div>
    </div>
    <div class="divider"></div>
    <div class="details">
      <h1 class="person-name">LENA OKAFOR</h1>
      <p class="person-title">Chief Financial Officer</p>
      <ul class="contact">
        <li>
          <svg viewBox="0 0 24 24"><path d="M6.6 10.8a15.2 15.2 0 0 0 6.6 6.6l2.2-2.2c.3-.3.7-.4 1-.2 1.1.4 2.3.6 3.6.6.6 0 1 .4 1 1V20c0 .6-.4 1-1 1A17 17 0 0 1 3 4c0-.6.4-1 1-1h3.5c.6 0 1 .4 1 1 0 1.3.2 2.5.6 3.6.1.3 0 .7-.2 1z"/></svg>
          780-555-0162
        </li>
        <li>
          <svg viewBox="0 0 24 24"><path d="M2 5h20v2l-10 6L2 7z"/><path d="M2 9l10 6 10-6v10H2z"/></svg>
          lenaokafor@marlbeckgroup.example
        </li>
        <li>
          <svg viewBox="0 0 24 24"><circle cx="12" cy="12" r="10"/><path d="M7 8c2 0 3 1 3 3s-2 2-2 4M15 5c0 2 2 2 3 4M14 19c0-2 1-3 3-3" stroke="#fff" stroke-width="1.6" fill="none"/></svg>
          marlbeckgroup.example
        </li>
      </ul>
    </div>
  </section>

  <section class="card card-back">
    <div class="back-brand">
      <div class="brand-mark"></div>
      <div class="brand-name">MARLBECK</div>
    </div>
    <p class="back-web">WWW.MARLBECKGROUP.EXAMPLE</p>
  </section>
</body>
</html>
```